EPS Recycling Rpt

Our annual recycling rate report needs a tune up. Our organization helps faciltate expanded polystyrene (EPS) recycling and this 4-page report highlights growth trends and useful information to help readers understand the dynamics of EPS recycling. We need a designer that can recreate the brochure we've published over the past several years with some minor adjustments to accomodate new content.

A PDF of the 2012 report is attached. Header text should reflect 2013 in all cases. Please pay close attention to the new placement of the copy as indicated in the Word file (also attached) as it has been significantly modified from the 2012 version. The color pallette for our branding is provided. Contact us with any questions.

```html
<!DOCTYPE html>
<html lang="en">
<head>
<meta charset="utf-8">
<title>2013 EPS Recycling Rate Report – Cover</title>
<link rel="stylesheet" href="https://fonts.googleapis.com/css2?family=Montserrat:wght@400;600&display=swap">
<style>
  :root {
    --backdrop: #e4e4e4;
    --paper: #ffffff;
    --gold: #a8781e;
    --olive: #9aa02a;
    --bead-light: #e3e8ec;
    --bead-mid: #b3bec8;
    --bead-dark: #8d9ba7;
    --text-light: #ffffff;
  }
  * { box-sizing: border-box; margin: 0; padding: 0; }
  html, body {
    width: 1200px;
    height: 803px;
    overflow: hidden;
    background: var(--backdrop);
    font-family: "Montserrat", sans-serif;
  }
  .report-cover {
    position: absolute;
    left: 349px;
    top: 57px;
    width: 464px;
    height: 690px;
    background: var(--paper);
  }
  .brand-name {
    position: absolute;
    left: 34px;
    top: 62px;
    color: var(--gold);
    font-weight: 400;
    font-size: 22px;
    line-height: 1.15;
  }
  .hero-image {
    position: absolute;
    left: 0;
    top: 143px;
    width: 464px;
    height: 357px;
    background:
      radial-gradient(circle at 30% 35%, var(--bead-light) 0%, transparent 45%),
      radial-gradient(circle at 75% 70%, var(--bead-light) 0%, transparent 40%),
      linear-gradient(160deg, var(--bead-mid) 0%, var(--bead-dark) 60%, var(--bead-mid) 100%);
  }
  .title-block {
    position: absolute;
    left: 294px;
    top: 370px;
    width: 170px;
    height: 120px;
    background: var(--olive);
    color: var(--text-light);
    padding: 14px 0 0 11px;
  }
  .title-year {
    font-weight: 400;
    font-size: 40px;
    line-height: 1;
    letter-spacing: 0.5px;
  }
  .title-line {
    font-size: 11.5px;
    line-height: 1.35;
    letter-spacing: 0.3px;
  }
  .title-line.strong { font-weight: 600; }
  .title-year + .title-line { margin-top: 9px; }
  .accent-bar, .thumb {
    position: absolute;
    top: 538px;
    height: 98px;
  }
  .accent-bar { background: var(--gold); }
  .accent-bar.left { left: 0; width: 19px; }
  .accent-bar.right { left: 430px; width: 34px; }
  .thumb.foam-pile { left: 30px; width: 122px; background: linear-gradient(135deg, #d9d4cb, #b8aa95 55%, #8d7a66); }
  .thumb.site-worker { left: 162px; width: 122px; background: linear-gradient(160deg, #bfc9d2, #8b98a3 50%, #4b5d7a); }
  .thumb.recycle-hands { left: 295px; width: 123px; background: radial-gradient(circle at 50% 50%, #b8d98a, #6fa33b 60%, #3f7a2a); }
</style>
</head>
<body>
  <main class="report-cover">
    <header class="brand-name">Foam Recovery<br>Council</header>

    <div class="hero-image" role="img" aria-label="Close-up photograph of white expanded polystyrene beads"></div>

    <section class="title-block">
      <div class="title-year">2013</div>
      <div class="title-line">EPS RECYCLING</div>
      <div class="title-line strong">RATE REPORT</div>
    </section>

    <div class="accent-bar left"></div>
    <div class="thumb foam-pile" role="img" aria-label="Photograph of a pile of collected foam packaging"></div>
    <div class="thumb site-worker" role="img" aria-label="Photograph of a worker in a hard hat and safety vest at a recycling facility"></div>
    <div class="thumb recycle-hands" role="img" aria-label="Photograph of hands holding a green recycling symbol against foliage"></div>
    <div class="accent-bar right"></div>
  </main>
</body>
</html>
```